ORVA CRM website - sleek, sophisticated, uplifting

ORVA Center for Regenerative Medicine is a cutting-edge medical clinic aimed at providing treatment for various chronic conditions and help people stave off the declines usually associated with aging. We utilize the latest technology in regenerative medicine to help people with autoimmune conditions, musculoskeletal problems and chronic pain, neurodegenerative conditions, male enhancement, facial rejuvenation and hair restoration, etc. We provide personalized medicine, through highly compassionate and competent doctors and staff.

please look at my current website which is not focused on regenerative medicine, but some contents can stay, as far as the philosophy of the treatment: www.plmwellnessgroup.example. But the reason I am changing the name of the clinic is because the focus of the medical practice is shifted entirely to "regenerative medicine" - using the body's own healing mechanism such as stem cells and growth factors...

Please DO NOT recycle old graphics and pictures. I want this site to be brand new, fresh and original.

Would like the website to be more sophisticated and nicer-looking than this website: www.vantrelo.example

Target Market(s)

People who care a great deal about their health (above age 35), wants to prevent declines in their looks and health as they are getting older. Generally high income sector of the society that can afford self-pay (no insurance accepted) expensive stem cell treatment ranging from $4000 to $20,000.

Industry/Entity Type

Healthcare

Coding

Coded - Design and coding required

Number of Pages Required

5+ page

Font styles to use
Sans Serif
Other font styles liked:
• Al Bayan, Avenir, Didot, Open Sans or Tsukushi A Round Gothic for central text, but may use Chalkboard for titles, or others as seen fit

Colors

Designer to choose colors to be used in the design.

Requirements
Must have
• Ultra modern look, very clean & sleek images and layout, portraying a sense of sophistication and confidence. Works beautifully well with existing logo. Give a sense that the clinic employs cutting-edge science, and provide highly competent & compassionate services.
• More sophisticated and nicer-looking than this website: www.vantrelo.example
Nice to have
• many pages and links to science articles
Should not have
• fonts too playful or hard to read.

```html
<!DOCTYPE html>
<html lang="en">
<head>
<meta charset="utf-8">
<title>ORVA Center for Regenerative Medicine</title>
<link href="https://fonts.googleapis.com/css2?family=Open+Sans:wght@400;600;700&display=swap" rel="stylesheet">
<style>
:root{
  --gold:#c9992c;
  --gold-dark:#b48624;
  --gold-field:#a98222;
  --ink:#444;
  --muted:#777;
  --light:#ececec;
  --card-head:#d6d6d6;
  --dark:#2b2d31;
  --footer:#333;
  --white:#fff;
}
*{margin:0;padding:0;box-sizing:border-box}
html,body{width:1200px;height:4110px;overflow:hidden}
body{font-family:"Open Sans",sans-serif;color:var(--ink);background:var(--white);position:relative}
.abs{position:absolute}
.header{top:0;left:0;width:1200px;height:137px;background:var(--white)}
.brand{left:0;width:1200px;top:44px;text-align:center;font-size:38px;font-weight:700;color:var(--gold);letter-spacing:3px}
.brand-sub{left:0;width:1200px;top:98px;text-align:center;font-size:12px;color:var(--muted)}
.nav{top:137px;left:0;width:1200px;height:49px;background:var(--gold)}
.nav ul{list-style:none;display:flex;margin-left:77px;height:49px}
.nav li{color:var(--white);font-size:17px;padding:0 18px;line-height:49px}
.nav li.active{background:#6e6e6e}
.hero{top:186px;left:0;width:1200px;height:587px;background:linear-gradient(120deg,#dfe9f0 0%,#9fc3da 40%,#3d7fae 75%,#1e4f78 100%)}
.hero-title{top:440px;left:0;width:1200px;text-align:center;color:var(--white);font-size:50px;font-weight:400}
.hero-rule{height:2px;background:rgba(201,153,44,.9);left:200px;width:800px}
.welcome-title{top:805px;width:1200px;text-align:center;color:var(--gold);font-size:32px;font-weight:700}
.welcome-sub{top:858px;width:1200px;text-align:center;font-size:14px;color:var(--muted)}
.cond{font-size:17px;color:#555;line-height:1.5}
.cond.left{text-align:right;width:250px;left:30px}
.cond.right{left:923px;width:230px}
.icon{width:63px;height:63px;background:var(--gold);display:flex;align-items:center;justify-content:center}
.hand{left:452px;top:959px;width:274px;height:386px;background:linear-gradient(180deg,#fff 0%,#f3e2d4 55%,#e6c7b1 100%)}
.services{top:1345px;left:0;width:1200px;height:737px;background:var(--light)}
.section-title{width:1200px;text-align:center;font-size:40px;font-weight:600}
.section-title .g{color:var(--gold)}
.card{width:230px;height:265px}
.card-head{height:82px;background:var(--card-head);text-align:center;padding-top:38px;font-size:18px;color:#555;position:relative}
.card-head::before{content:"";position:absolute;top:18px;left:95px;width:40px;height:2px;background:var(--gold)}
.card-img{height:183px}
.band{top:2082px;left:0;width:1200px;height:129px;background:var(--gold);color:var(--white);text-align:center;font-size:26px;font-weight:700;line-height:1.5;padding-top:25px}
.about{top:2211px;left:0;width:1200px;height:447px;background:linear-gradient(90deg,#f6f6f6 0%,#eceff1 100%)}
.doctor{left:90px;top:2225px;width:330px;height:433px;background:linear-gradient(180deg,#e7e9ec 0%,#d4d7dc 60%,#c9ccd1 100%)}
.about-text{left:520px;top:2290px;width:600px;font-size:15px;line-height:1.6;color:#666}
.about-text p{margin-bottom:14px}
.learn{left:520px;top:2488px;font-size:14px;color:var(--gold);font-weight:600;display:flex;align-items:center;gap:10px}
.tabs{top:2845px;left:77px;width:1046px;display:flex;gap:40px;font-size:16px;color:#555}
.tabs span.on{border-top:2px solid #999;border-bottom:2px solid #999;padding:6px 0}
.tabs span{padding:8px 0}
.product{width:241px;height:326px;border:2px solid #ddd;background:var(--white);text-align:center}
.product.sel{border-color:#ccc;box-shadow:0 0 8px rgba(0,0,0,.18)}
.bottle{width:110px;height:160px;margin:40px auto 0;border-radius:14px}
.p-name{margin-top:38px;font-size:18px;color:#555}
.p-brand{font-size:13px;color:var(--muted);margin-top:4px}
.p-rule{width:200px;height:1px;background:#ddd;margin:6px auto 0}
.arrow-btn{width:38px;height:38px;background:#e3e3e3;display:flex;align-items:center;justify-content:center}
.contact{top:3419px;left:0;width:1200px;height:274px;background:linear-gradient(120deg,#3a3d42 0%,#26282c 100%)}
.cbox{top:3466px;width:334px;height:178px;background:#f2f2f2;display:flex;padding:48px 0 0 30px;gap:22px}
.cbox h3{font-size:26px;font-weight:400;color:#555}
.cbox p{font-size:14px;color:var(--muted);line-height:1.5;margin-top:6px}
.cbox p.email{font-size:13px}
.form{top:3693px;left:0;width:1200px;height:293px;background:var(--gold)}
.field{height:41px;background:var(--gold-field);color:#f3e8cf;font-size:14px;padding:10px 18px}
.submit{background:var(--white);color:var(--gold);font-weight:700;text-align:center;font-size:18px;padding-top:8px}
.footer{top:3986px;left:0;width:1200px;height:124px;background:var(--footer);color:#ddd}
.f-links{left:77px;top:4012px;display:flex;gap:26px;font-size:14px;color:#ddd}
.copy{left:77px;top:4060px;font-size:14px;color:#ccc}
.social{top:4048px;left:982px;display:flex;gap:10px}
.social span{width:40px;height:40px;border-radius:50%;background:var(--white)}
</style>
</head>
<body>

<header class="abs header"></header>
<div class="abs brand">ORVA</div>
<div class="abs brand-sub">Center for Regenerative Medicine</div>

<nav class="abs nav">
  <ul>
    <li class="active">Home</li><li>Services</li><li>The Science</li><li>Forum</li><li>professional-Grade Supplements</li><li>Blog</li><li>Contact</li>
  </ul>
</nav>

<section class="abs hero" role="img" aria-label="Scientist in safety glasses looking into a microscope in a blue-lit lab"></section>
<div class="abs hero-rule" style="top:433px"></div>
<h1 class="abs hero-title">Center For Regenerative Medicine</h1>
<div class="abs hero-rule" style="top:512px"></div>

<h2 class="abs welcome-title">Welcome Visitor!</h2>
<p class="abs welcome-sub">We utilize the latest technology in regenerative medicine to help people with</p>

<div class="abs cond left" style="top:956px">Autoimmune<br>Conditions</div>
<div class="abs icon" style="left:307px;top:950px"><svg width="32" height="32" viewBox="0 0 32 32" fill="#fff"><circle cx="16" cy="9" r="6"/><rect x="7" y="17" width="18" height="13" rx="3"/></svg></div>
<div class="abs cond left" style="top:1084px">Musculoskeletal<br>Problems</div>
<div class="abs icon" style="left:307px;top:1078px"><svg width="32" height="32" viewBox="0 0 32 32" fill="#fff"><circle cx="16" cy="6" r="4"/><rect x="12" y="11" width="8" height="11"/><rect x="5" y="12" width="6" height="3"/><rect x="21" y="12" width="6" height="3"/><rect x="12" y="22" width="3" height="8"/><rect x="17" y="22" width="3" height="8"/></svg></div>
<div class="abs cond left" style="top:1222px">Chronic Pain</div>
<div class="abs icon" style="left:307px;top:1203px"><svg width="32" height="32" viewBox="0 0 32 32" fill="none" stroke="#fff" stroke-width="2"><path d="M10 4v10c0 8-4 10-4 14M22 4v10c0 8 4 10 4 14M16 8v20"/></svg></div>

<div class="abs hand" role="img" aria-label="Hand with a raised index finger touching a glowing screen icon"></div>

<div class="abs icon" style="left:830px;top:950px"><svg width="32" height="32" viewBox="0 0 32 32" fill="none" stroke="#fff" stroke-width="2"><circle cx="16" cy="16" r="12"/><path d="M10 12c3 0 3 4 6 4s3-4 6-4M10 20c3 0 3-3 6-3s3 3 6 3"/></svg></div>
<div class="abs cond right" style="top:956px">Neurodegenerative<br>Conditions</div>
<div class="abs icon" style="left:830px;top:1078px"><svg width="32" height="32" viewBox="0 0 32 32" fill="none" stroke="#fff" stroke-width="2"><circle cx="16" cy="8" r="4"/><circle cx="9" cy="23" r="5"/><circle cx="23" cy="23" r="5"/></svg></div>
<div class="abs cond right" style="top:1096px">Male Enhancement</div>
<div class="abs icon" style="left:830px;top:1203px"><svg width="32" height="32" viewBox="0 0 32 32" fill="#fff"><path d="M26 4C12 4 6 12 6 20c0 4 2 8 6 8 8 0 14-10 14-24z"/></svg></div>
<div class="abs cond right" style="top:1206px">Facial Rejuvenation and<br>Hair restoration</div>

<section class="abs services"></section>
<h2 class="abs section-title" style="top:1378px"><span class="g">Our Services</span></h2>

<div class="abs card" style="left:77px;top:1458px"><div class="card-head">Micronutrients</div><div class="card-img" role="img" aria-label="Colourful fruits and vegetables" style="background:linear-gradient(135deg,#c23a1e,#e6a21f 45%,#4f8a2a)"></div></div>
<div class="abs card" style="left:351px;top:1458px"><div class="card-head">Hormones</div><div class="card-img" role="img" aria-label="Glowing purple bokeh lights" style="background:radial-gradient(circle at 40% 50%,#e07ad8,#6a2c9c 60%,#2a123e)"></div></div>
<div class="abs card" style="left:622px;top:1458px"><div class="card-head">Food &amp; Gut</div><div class="card-img" role="img" aria-label="Healthy food spread on a table" style="background:linear-gradient(135deg,#9a7a5a,#5e7d3c 50%,#c9a97a)"></div></div>
<div class="abs card" style="left:893px;top:1458px"><div class="card-head">Weight Loss</div><div class="card-img" role="img" aria-label="Waist with a measuring tape" style="background:linear-gradient(135deg,#bfe0ef,#6fb3d6 50%,#e9c9b3)"></div></div>
<div class="abs card" style="left:77px;top:1762px"><div class="card-head">Addiction</div><div class="card-img" role="img" aria-label="Dark scene of substance use" style="background:linear-gradient(135deg,#4a4a4a,#1e1e1e 60%,#7a6a5a)"></div></div>
<div class="abs card" style="left:351px;top:1762px"><div class="card-head">Toxic Elemnets</div><div class="card-img" role="img" aria-label="Periodic table of elements in warm light" style="background:linear-gradient(135deg,#2a4a6a,#c27a2a 55%,#3a2a1a)"></div></div>
<div class="abs card" style="left:622px;top:1762px"><div class="card-head">Genetic Tests</div><div class="card-img" role="img" aria-label="Lab pipette filling test tubes" style="background:linear-gradient(135deg,#eef3f7,#b9cbd8 55%,#7a98ae)"></div></div>
<div class="abs card" style="left:893px;top:1762px"><div class="card-head">Stem Cells</div><div class="card-img" role="img" aria-label="Blue microscopic stem cells" style="background:radial-gradient(circle at 50% 50%,#7fd3f5,#1c7fc4 55%,#0a2e5c)"></div></div>

<div class="abs band">Our health is multi-faceted, and our vibrancy is built on our<br>biological, psychological and spiritual wellbeing.</div>
<svg class="abs" style="top:2210px;left:570px" width="60" height="26" viewBox="0 0 60 26"><polygon points="0,0 60,0 30,26" fill="#c9992c"/></svg>

<section class="abs about"></section>
<div class="abs doctor" role="img" aria-label="Smiling physician in a white coat with a stethoscope"></div>
<div class="abs about-text">
  <p>ORVA provides a new kind of healthcare that represents the future; we foster health in a holistic, preventative, and science-driven manner. We utilize the most up-to-date scientific data, treat each person as a unique individual, with unique micronutrient requirements, genetic codes, gut flora compositions, history of toxic exposures, and hormone variations.</p>
  <p>Through optimizing these essential interlinking aspects of person's health, the process of aging can be slowed, and people can live longer and more vibrant lives.</p>
</div>
<div class="abs learn"><svg width="22" height="22" viewBox="0 0 22 22" fill="none" stroke="#c9992c" stroke-width="2"><circle cx="11" cy="11" r="9"/><path d="M9 7l4 4-4 4"/></svg>LEARN MORE</div>

<h2 class="abs section-title" style="top:2745px"><span class="g">professional-Grade</span> <span style="color:#555">Supplements</span></h2>
<div class="abs tabs"><span class="on">Nutritional Supplements</span><span>Vitamins &amp; Minerals</span><span>Herbs</span><span>Homeopathy</span><span>Personal Care &amp; Lifestyle</span><span>Animal Health</span></div>

<div class="abs product" style="left:77px;top:2937px"><div class="bottle" role="img" aria-label="Supplement jar" style="background:linear-gradient(180deg,#2f6e3a 0 18%,#f5f5f0 18%)"></div><div class="p-name">Celvane</div><div class="p-rule"></div><div class="p-brand">Norwell Labs</div></div>
<div class="abs product" style="left:350px;top:2937px"><div class="bottle" role="img" aria-label="Supplement bottle" style="background:linear-gradient(180deg,#8c2a1a 0 18%,#e9a23a 18%)"></div><div class="p-name">Ostrelle</div><div class="p-rule"></div><div class="p-brand">Norwell Labs</div></div>
<div class="abs product sel" style="left:616px;top:2937px"><div class="bottle" role="img" aria-label="Dark liquid supplement bottle" style="width:70px;background:linear-gradient(180deg,#222 0 15%,#1d2b4e 15%)"></div><div class="p-name">Liposomal Vitamin C</div><div class="p-rule"></div><div class="p-brand">Calder Nutrition</div></div>
<div class="abs product" style="left:882px;top:2937px"><div class="bottle" role="img" aria-label="Supplement jar" style="background:linear-gradient(180deg,#7a1620 0 18%,#b0202e 18%)"></div><div class="p-name">Draventa</div><div class="p-rule"></div><div class="p-brand">Norwell Labs</div></div>

<div class="abs arrow-btn" style="left:77px;top:3305px"><svg width="14" height="14" viewBox="0 0 14 14"><path d="M9 2L4 7l5 5" fill="none" stroke="#888" stroke-width="2"/></svg></div>
<div class="abs arrow-btn" style="left:1085px;top:3305px"><svg width="14" height="14" viewBox="0 0 14 14"><path d="M5 2l5 5-5 5" fill="none" stroke="#888" stroke-width="2"/></svg></div>

<section class="abs contact" role="img" aria-label="Darkened laptop and workspace backdrop"></section>
<div class="abs cbox" style="left:77px"><svg width="48" height="60" viewBox="0 0 48 60" fill="none" stroke="#c9992c" stroke-width="2.5"><path d="M24 58S6 34 6 22a18 18 0 0136 0c0 12-18 36-18 36z"/><circle cx="24" cy="22" r="7"/></svg><div><h3>Address</h3><p>2140 Linden Crest Road Suite<br>210 Brookvale CA 90000</p></div></div>
<div class="abs cbox" style="left:433px"><svg width="52" height="52" viewBox="0 0 52 52" fill="none" stroke="#c9992c" stroke-width="2.5"><path d="M14 4l8 12-5 5c3 6 8 11 14 14l5-5 12 8-5 8C26 46 6 26 6 9z"/></svg><div><h3>Phone</h3><p>+1 555 014 2286</p></div></div>
<div class="abs cbox" style="left:789px"><svg width="52" height="48" viewBox="0 0 52 48" fill="none" stroke="#c9992c" stroke-width="2.5"><path d="M4 20L26 4l22 16v24H4z"/><path d="M4 20l22 14 22-14"/></svg><div><h3>Email</h3><p class="email">info@plmwellnessgroup.example</p></div></div>

<section class="abs form"></section>
<div class="abs field" style="left:230px;top:3767px;width:362px">Name</div>
<div class="abs field" style="left:230px;top:3819px;width:362px">Email</div>
<div class="abs field" style="left:230px;top:3871px;width:362px">Phone</div>
<div class="abs field" style="left:614px;top:3767px;width:362px;height:93px">Message</div>
<div class="abs field submit" style="left:614px;top:3871px;width:362px">SUBMIT</div>

<footer class="abs footer"></footer>
<div class="abs f-links"><span>Home</span><span>Services</span><span>The Science</span><span>Forum</span><span>professional-Grade Supplements</span><span>Blog</span><span>Contact</span></div>
<div class="abs copy">©ORVA Center For Regenerative Medicine - 2018. All Rights Reserved.</div>
<div class="abs social" aria-hidden="true"><span></span><span></span><span></span></div>

</body>
</html>
```